Tranquil Pathway Business Card

Logo attached. (will be printing onto thick white/off white textured card)

Double sided business card for two Therapists working at Tranquil Pathway.

Require one design, but with different name and mobile numbers on each card.

Target Market(s)

Medical, Health

Industry/Entity Type

Business

Contact Information for Business Card

Need one business card design, but a separate card for each person - Colin Marchetti and Marieke de Boeckx.

FRONT OF CARD

Logo

Name (Colin Marchetti on one card, Marieke de Boeckx on the other)
Professional Clinical Hypnotherapist

Consulting Rooms (Near Lindqvist Hospital)
482 Brackenfield Road
Dunmore VIC 3987

Colin@TranquilPathway.example.au OR Marieke@TranquilPathway.example.au

Mobile: 0455 872 604 (for Colin) OR
Mobile: 0467 290 518 (for Marieke)

BACK OF CARD

Logo

Website: www.TranquilPathway.example.au

Phone: 1300 958 471

Requirements
Must have
• Text and logo only. No additiional graphics.

```html
<!DOCTYPE html>
<html lang="en">
<head>
<meta charset="utf-8">
<title>Tranquil Pathway Business Card</title>
<link href="https://fonts.googleapis.com/css2?family=EB+Garamond:wght@400;600&display=swap" rel="stylesheet">
<style>
  :root {
    --backdrop: #d3d6d8;
    --card: #f4f3f0;
    --navy: #1f2a5a;
    --ink: #55575c;
    --rule: #8a8c90;
  }
  * { box-sizing: border-box; margin: 0; padding: 0; }
  html, body { width: 1200px; height: 873px; overflow: hidden; }
  body {
    background: var(--backdrop);
    font-family: "EB Garamond", Georgia, serif;
    display: flex; align-items: center; justify-content: center; gap: 40px;
  }
  .card {
    position: relative;
    width: 540px; height: 330px;
    background: var(--card);
    box-shadow: 0 6px 18px rgba(0,0,0,0.12);
  }
  .top-rule, .bottom-rule {
    position: absolute; left: 0; right: 0; height: 1px; background: var(--rule);
  }
  .top-rule { top: 62px; }
  .bottom-rule { top: 282px; }
  .logo {
    position: absolute; display: flex; align-items: center; gap: 12px;
  }
  .logo-dot {
    width: 54px; height: 54px; border-radius: 50%; background: var(--navy); flex: none;
  }
  .logo-divider { width: 1px; height: 54px; background: var(--rule); }
  .logo-name {
    color: var(--navy); font-weight: 600; font-size: 21px; line-height: 1.05;
    letter-spacing: 1.5px; text-transform: uppercase;
  }
  .front .logo { left: 26px; top: 108px; }
  .person { position: absolute; left: 292px; top: 82px; }
  .person-name { color: var(--navy); font-size: 21px; }
  .person-role { color: var(--ink); font-size: 12.5px; border-bottom: 1px solid var(--rule); padding-bottom: 2px; }
  .contact {
    position: absolute; left: 268px; top: 148px;
    border-left: 1px solid var(--navy); padding-left: 12px;
    color: var(--ink); font-size: 13px; line-height: 1.3;
  }
  .contact-row { display: flex; gap: 8px; margin-bottom: 12px; }
  .contact-row:last-child { margin-bottom: 0; }
  .icon { width: 12px; height: 14px; flex: none; margin-top: 2px; }
  .back .logo { left: 150px; top: 104px; }
  .back-details {
    position: absolute; left: 0; right: 0; top: 180px; text-align: center;
  }
  .website { color: var(--navy); font-size: 17px; }
  .phone { color: var(--ink); font-size: 17px; margin-top: 14px; display: inline-flex; align-items: center; gap: 7px; }
</style>
</head>
<body>
  <section class="card front">
    <div class="top-rule"></div>
    <div class="logo">
      <div class="logo-dot"></div>
      <div class="logo-divider"></div>
      <div class="logo-name">Tranquil<br>Pathway</div>
    </div>
    <div class="person">
      <div class="person-name">Marieke de Boeckx</div>
      <div class="person-role">Professional Clinical Hypnotherapist</div>
    </div>
    <div class="contact">
      <div class="contact-row">
        <svg class="icon" viewBox="0 0 12 14"><path d="M6 1a4 4 0 0 0-4 4c0 3 4 8 4 8s4-5 4-8a4 4 0 0 0-4-4z" fill="none" stroke="#1f2a5a" stroke-width="1.3"/><circle cx="6" cy="5" r="1.4" fill="#1f2a5a"/></svg>
        <div>Consulting Rooms (Nr. Lindqvist Hospital)<br>482 Brackenfield Road<br>Dunmore VIC 3987</div>
      </div>
      <div class="contact-row">
        <svg class="icon" viewBox="0 0 12 14"><rect x="2.5" y="1" width="7" height="12" rx="1.2" fill="none" stroke="#1f2a5a" stroke-width="1.2"/><circle cx="6" cy="11" r="0.8" fill="#1f2a5a"/></svg>
        <div>0467 290 518</div>
      </div>
      <div class="contact-row">
        <svg class="icon" viewBox="0 0 12 14"><rect x="0.5" y="3" width="11" height="8" fill="#1f2a5a"/><path d="M0.8 3.3 6 7.5l5.2-4.2" fill="none" stroke="#f4f3f0" stroke-width="1"/></svg>
        <div>Marieke@TranquilPathway.example.au</div>
      </div>
    </div>
  </section>

  <section class="card back">
    <div class="top-rule"></div>
    <div class="logo">
      <div class="logo-dot"></div>
      <div class="logo-divider"></div>
      <div class="logo-name">Tranquil<br>Pathway</div>
    </div>
    <div class="back-details">
      <div class="website">www.TranquilPathway.example.au</div>
      <div class="phone">
        <svg width="13" height="13" viewBox="0 0 13 13"><path d="M3 1l2 2.5-1.2 1.4c.8 1.7 2.2 3.1 3.9 3.9L9.1 7.6 11.6 9.6 10.4 11.8C5.8 11.5 1.5 7.2 1.2 2.6z" fill="#1f2a5a"/></svg>
        1300 958 471
      </div>
    </div>
    <div class="bottom-rule"></div>
  </section>
</body>
</html>
```